Tidewell Recovery Business Card Design

Professional and clean design. The design colors should flow with the logo. Two-sided card with the website on the back which is:

www.TidewellRecovery.example.

"Specializing in Water Damage Restoration"

On the front I need the name, email, phone, and logo.

Name: Dorian Vashti
Email: Dorian@TidewellRecovery.example
Phone: 555-318-2046 for now

I only have the Preview and Thumbnail right now but should have the source files uploaded within a day or two.

Target Market(s)

Flood victims, home owners with water damage from busted pipes etc...

Industry/Entity Type

Business

Contact Information for Business Card

Name: Dorian Vashti

Font styles to use
Serif
Sans Serif

```html
<!DOCTYPE html>
<html lang="en">
<head>
<meta charset="utf-8">
<title>Tidewell Recovery – Business Card</title>
<link rel="stylesheet" href="https://fonts.googleapis.com/css2?family=Cinzel:wght@600&family=Open+Sans:wght@400;700&display=swap">
<style>
  :root {
    --bg: #ecebe8;
    --white: #ffffff;
    --paper: #f4f5f5;
    --blue: #2ba6d4;
    --blue-light: #36bde0;
    --blue-deep: #1a86b8;
    --blue-pale: #7fcbe8;
    --ink-light: #ffffff;
  }
  * { box-sizing: border-box; margin: 0; padding: 0; }
  html, body { width: 1200px; height: 780px; overflow: hidden; }
  body {
    background: var(--bg);
    font-family: "Open Sans", Arial, sans-serif;
    display: flex;
    align-items: center;
    justify-content: center;
    gap: 40px;
  }
  .card {
    position: relative;
    width: 540px;
    height: 309px;
    border-radius: 4px;
    overflow: hidden;
    box-shadow: 0 6px 18px rgba(0,0,0,0.18);
  }

  /* Front */
  .card-front { background: linear-gradient(135deg, var(--white), var(--paper)); }
  .card-front .wave { position: absolute; inset: 0; width: 100%; height: 100%; }
  .brand-block {
    position: absolute;
    left: 26px;
    top: 96px;
    width: 290px;
    color: var(--blue);
  }
  .brand-row { display: flex; align-items: center; gap: 12px; }
  .brand-dot {
    width: 46px; height: 46px; border-radius: 50%;
    background: var(--blue); flex: none;
  }
  .brand-name {
    font-family: "Cinzel", "Times New Roman", serif;
    font-weight: 600;
    font-size: 23px;
    letter-spacing: 1px;
    line-height: 1.15;
    color: var(--blue);
  }
  .tagline {
    margin-top: 14px;
    font-size: 12.5px;
    color: var(--blue);
    letter-spacing: 0.2px;
  }
  .contact {
    position: absolute;
    left: 340px;
    top: 82px;
    color: var(--ink-light);
  }
  .contact-name { font-weight: 700; font-size: 17px; margin-bottom: 12px; }
  .contact-line {
    display: flex; align-items: center; gap: 8px;
    font-size: 10.5px; line-height: 1; margin-bottom: 9px;
  }
  .contact-line svg { width: 14px; height: 14px; flex: none; }

  /* Back */
  .card-back {
    background: radial-gradient(ellipse at 45% 30%, var(--blue-light), var(--blue) 55%, var(--blue-deep));
    color: var(--ink-light);
    display: flex; flex-direction: column; align-items: center; justify-content: center;
    text-align: center;
  }
  .card-back .brand-row { gap: 14px; }
  .card-back .brand-dot { background: var(--white); width: 52px; height: 52px; }
  .card-back .brand-name { color: var(--white); font-size: 26px; }
  .card-back .tagline { color: var(--white); margin-top: 14px; }
  .back-web { margin-top: 22px; font-size: 12px; letter-spacing: 0.3px; }
  .back-rule {
    position: absolute; bottom: 22px; height: 1px; background: rgba(255,255,255,0.75); width: 90px;
  }
  .back-rule.left { left: 30px; }
  .back-rule.right { right: 30px; }
</style>
</head>
<body>

  <section class="card card-front" aria-label="Business card front">
    <svg class="wave" viewBox="0 0 540 309" preserveAspectRatio="none" aria-hidden="true">
      <path d="M262 0 C330 60 350 190 318 309 L540 309 L540 0 Z" fill="var(--blue)"/>
      <path d="M250 0 C318 60 338 190 304 309 L312 309 C344 190 324 60 258 0 Z" fill="var(--blue-pale)"/>
    </svg>

    <div class="brand-block">
      <div class="brand-row">
        <span class="brand-dot"></span>
        <span class="brand-name">TIDEWELL RECOVERY</span>
      </div>
      <p class="tagline">Specializing in Water Damage Restoration</p>
    </div>

    <div class="contact">
      <p class="contact-name">Dorian Vashti</p>
      <p class="contact-line">
        <svg viewBox="0 0 16 16" aria-hidden="true"><rect width="16" height="16" rx="2" fill="#fff" fill-opacity="0.9"/><path d="M5 3.5l1.6 2.2-1 1.1a6 6 0 0 0 3.6 3.6l1.1-1 2.2 1.6-.8 1.8C7.5 12.6 3.4 8.5 3.2 4.3z" fill="var(--blue)"/></svg>
        555-318-2046
      </p>
      <p class="contact-line">
        <svg viewBox="0 0 16 16" aria-hidden="true"><rect width="16" height="16" rx="2" fill="#fff" fill-opacity="0.9"/><rect x="3" y="4.5" width="10" height="7" fill="none" stroke="var(--blue)" stroke-width="1.2"/><path d="M3 4.5l5 4 5-4" fill="none" stroke="var(--blue)" stroke-width="1.2"/></svg>
        Dorian@TidewellRecovery.example
      </p>
      <p class="contact-line">
        <svg viewBox="0 0 16 16" aria-hidden="true"><rect width="16" height="16" rx="2" fill="#fff" fill-opacity="0.9"/><circle cx="8" cy="8" r="4.8" fill="none" stroke="var(--blue)" stroke-width="1.1"/><ellipse cx="8" cy="8" rx="2" ry="4.8" fill="none" stroke="var(--blue)" stroke-width="1"/><path d="M3.2 8h9.6" stroke="var(--blue)" stroke-width="1"/></svg>
        www.TidewellRecovery.example
      </p>
    </div>
  </section>

  <section class="card card-back" aria-label="Business card back">
    <div class="brand-row">
      <span class="brand-dot"></span>
      <span class="brand-name">TIDEWELL RECOVERY</span>
    </div>
    <p class="tagline">Specializing in Water Damage Restoration</p>
    <p class="back-web">www.TidewellRecovery.example</p>
    <span class="back-rule left"></span>
    <span class="back-rule right"></span>
  </section>

</body>
</html>
```